依頼詳細
PCとスマホデザインの両方納品をいただきますが、
まずはデザインイメージが確認しやすいPCページのみの提案をお願いします。
スマホページは当選者に納品時にお願いしたいと思います。
スマホサイズについて、表示は横幅375pxで作成し、
デザインデータは2倍の横幅750pxのカンバスサイズで作成してください。
(Retinaディスプレイに対応するため)
レスポンシブウェブデザインを意識したデザインでお願いします。

■サイトマップ
添付の画面遷移図をご確認ください。

■参考サイト
http://hoshizora-tetsuko.co.jp/

■内容について
鋳造部品等を製作する会社のサイトリニューアルになります。
既存サイト
http://www.senbeiseiko.com/kiyora/index.html

■素材写真
画像データについては、フリー素材から流用して
イメージ画像に当て込んでください。
足りない場合は、一旦他のサイトの写真をサンプルとして
入れてください。(サンプルなどの表記をお願いします)
また、購入が必要な写真などを利用した場合、
価格とサイト名を教えてください。

また、Lumera Photosで定期契約をしていますので、
Lumera Photosの画像は使用できます。
デザイン時はカンプ画像をお入れいただきますようお願いします。

■ワイヤーフレーム
https://mock.wirevista.net/view/1a2b3c4d-5e6f-4a7b-8c9d-0e1f2a3b4c5d-8812/?fullscreen
コンテンツの構成としてワイヤーフレームを作成しましたが
必ずしもワイヤーフレームの通りではなくて大丈夫です。
TOPページに配置するコンテンツを見ていただき、デザインは
デザイナーの皆様におまかせしたいと思います。

----------------------------------------------------------------------------
【制作物に対するお願い】

■フォントについて
・無料で使えるフォントで作成をお願いします。
・OSに紐づくフォントの使用は控えていただければと思います (ヒラギノなど)

ページ数
1ページ
希望イメージ
シンプル 複雑
単色 カラフル
暗い 明るい
日常 高級
遊び心 厳粛
未来的 伝統的
女性的 男性的
希望する色
アクセントカラー:茶色、もしくは青色
納品ファイル
• 高解像度JPG (.jpg)
• イラストレーター形式 (.ai)
• フォトショップ形式 (.psd)
補足説明
上記のいずれか1つ(アウトラインありとなしの2つ)と高解像度JPGを納品お願いします。
adobe XDでの納品も可能です。

```html
<!DOCTYPE html>
<html lang="ja">
<head>
<meta charset="UTF-8">
<title>清良伸銅株式会社</title>
<link rel="stylesheet" href="https://fonts.googleapis.com/css2?family=Noto+Serif+JP:wght@400;500;600;700&family=Noto+Sans+JP:wght@400;500;700&display=swap">
<style>
  :root{
    --navy:#0a1068;
    --navy-deep:#080d62;
    --ink:#333;
    --muted:#8a8a8a;
    --rule:#cfcfd4;
    --band:#d7d8e1;
    --white:#fff;
  }
  *{margin:0;padding:0;box-sizing:border-box}
  html,body{width:1200px;height:3154px;overflow:hidden;background:var(--white)}
  body{position:relative;font-family:"Noto Serif JP",serif;color:var(--ink)}
  .abs{position:absolute}
  .center{left:0;width:1200px;text-align:center}

  /* hero */
  .hero{left:0;top:0;width:1200px;height:675px;
    background:radial-gradient(ellipse at 62% 40%,#f39a2b 0%,#c2561a 18%,#5a2410 42%,#241410 70%,#120c0a 100%)}
  .nav{left:0;top:0;width:1200px;height:61px;background:rgba(40,36,36,.72)}
  .nav a{position:absolute;top:0;line-height:61px;color:var(--white);font-size:15px;text-decoration:none;transform:translateX(-50%)}
  .hero-copy{left:104px;top:226px;color:var(--white);font-size:34px;font-weight:500;line-height:49px;letter-spacing:1px}
  .hero-copy small{font-size:24px}
  .hero-en{left:104px;top:356px;color:var(--white);font-size:40px;font-weight:500}
  .hero-sub{left:104px;top:424px;color:var(--white);font-size:21px;font-weight:500}
  .scroll{left:1034px;top:606px;color:var(--white);font-size:10px;writing-mode:vertical-rl}

  /* section headings */
  .sec-title{color:var(--navy);font-size:26px;font-weight:600}
  .sec-sub{color:var(--muted);font-size:13px}

  .about-lead{font-size:19px;color:#222}
  .about-text{left:201px;top:904px;width:798px;font-size:9.5px;line-height:15px;color:#9a9a9a}

  .product{width:236px;height:235px;top:1129px}
  .product-name{top:1382px;font-size:15px;color:#444}
  .btn{display:block;height:37px;border-radius:19px;background:var(--navy);color:var(--white);
    font-size:13px;font-weight:600;text-align:center;line-height:37px;letter-spacing:.5px}
  .btn svg{position:absolute;right:22px;top:14px}

  .process{top:1630px;width:347px;height:290px;text-align:center;color:var(--white)}
  .process .en{position:absolute;left:0;width:100%;top:104px;font-size:15px}
  .process .ja{position:absolute;left:0;width:100%;top:126px;font-size:25px;font-weight:600}
  .process .pill{position:absolute;left:62px;top:173px;width:240px;height:37px;border-radius:19px;
    background:rgba(255,255,255,.28);line-height:37px;font-size:13px}

  .recruit-band{left:0;top:2056px;width:1200px;height:288px;background:var(--band)}
  .recruit-photo{left:600px;top:2014px;width:399px;height:267px;
    background:linear-gradient(160deg,#2b3c66 0%,#3c5a9a 35%,#c45a1e 70%,#2a2a3a 100%)}
  .recruit-text{left:231px;top:2204px;font-size:10px;color:#555}

  .news-rule{left:201px;width:798px;height:1px;background:var(--rule)}
  .news-date{left:231px;font-family:"Noto Sans JP",sans-serif;font-size:11px;color:#666}
  .news-title{left:231px;font-family:"Noto Sans JP",sans-serif;font-size:15px;font-weight:700;color:#555}

  .footer{left:0;top:2900px;width:1200px;height:254px;background:var(--navy-deep)}
  .footer a{position:absolute;top:95px;color:var(--white);font-size:14px;text-decoration:none}
  .footer a::before{content:"> ";font-size:12px}
  .copyright{left:0;top:213px;width:1200px;text-align:center;color:var(--white);font-size:9px}
</style>
</head>
<body>

<section class="abs hero" role="img" aria-label="溶けた金属を注ぐ取鍋と火花が散る鋳造現場の写真"></section>
<nav class="abs nav">
  <a href="#" style="left:380px">清良伸銅とは</a>
  <a href="#" style="left:503px">製品紹介</a>
  <a href="#" style="left:615px">製造案内</a>
  <a href="#" style="left:726px">採用情報</a>
  <a href="#" style="left:836px">お知らせ</a>
</nav>
<h1 class="abs hero-copy">75年の経験とノウハウ<br>あくなき探究心<small>が</small>つくりあげる</h1>
<p class="abs hero-en">Kiyora copper elongation</p>
<p class="abs hero-sub">Metal forging and manufaturing</p>
<div class="abs scroll">Scroll</div>
<svg class="abs" style="left:1046px;top:608px" width="12" height="36" viewBox="0 0 12 36"><path d="M1 0V34H11L5 28" fill="none" stroke="#fff" stroke-width="1"/></svg>

<!-- about -->
<h2 class="abs center sec-title" style="top:770px">清良伸銅について</h2>
<p class="abs center sec-sub" style="top:810px">About</p>
<p class="abs center about-lead" style="top:853px">一歩一歩積み重ね、磨き上げてきた伸銅技術と鍛造技術</p>
<p class="abs about-text">清良伸銅の歩みと技術の説明が入ります。清良伸銅の歩みと技術の説明が入ります。清良伸銅の歩みと技術の説明が入ります。清良伸銅の歩みと技術の説明が入ります。清良伸銅の歩みと技術の説明が入ります。清良伸銅の歩みと技術の説明が入ります。清良伸銅の歩みと技術の説明が入ります。清良伸銅の歩みと技術の説明が入ります。清良伸銅の歩みと技術の説明が入ります。清良伸銅の歩みと技術の説明が入ります。清良伸銅の歩みと技術の説明が入ります。清良伸銅の歩みと技術の説明が入ります。清良伸銅の歩みと技術の説明が入ります。清良伸銅の歩みと技術の説明が入ります。</p>

<!-- products -->
<h2 class="abs center sec-title" style="top:1043px">製品紹介</h2>
<p class="abs center sec-sub" style="top:1087px">Product</p>

<div class="abs product" style="left:201px;background:linear-gradient(160deg,#7a3a2a,#c98c74 50%,#5a2a22)" role="img" aria-label="並んだ銅製部品の写真"></div>
<div class="abs product" style="left:481px;background:linear-gradient(160deg,#5b4a2c,#c9b27a 50%,#4a3a22)" role="img" aria-label="積み重なった黄銅継手の写真"></div>
<div class="abs product" style="left:762px;background:linear-gradient(160deg,#6d6f73,#c4c6c9 50%,#8a8c90)" role="img" aria-label="鍛造したアルミ部品の写真"></div>

<p class="abs product-name" style="left:211px">銅製品</p>
<p class="abs product-name" style="left:491px">黄銅製品</p>
<p class="abs product-name" style="left:772px">鍛造加工</p>

<a class="abs btn" href="#" style="left:201px;top:1412px;width:239px">READ MORE<svg width="7" height="10" viewBox="0 0 7 10"><path d="M1 1l4 4-4 4" fill="none" stroke="#fff"/></svg></a>
<a class="abs btn" href="#" style="left:481px;top:1412px;width:239px">READ MORE<svg width="7" height="10" viewBox="0 0 7 10"><path d="M1 1l4 4-4 4" fill="none" stroke="#fff"/></svg></a>
<a class="abs btn" href="#" style="left:761px;top:1412px;width:239px">READ MORE<svg width="7" height="10" viewBox="0 0 7 10"><path d="M1 1l4 4-4 4" fill="none" stroke="#fff"/></svg></a>

<!-- process -->
<h2 class="abs center sec-title" style="top:1544px">製造案内</h2>
<p class="abs center sec-sub" style="top:1589px">Process＆Facility</p>

<div class="abs process" style="left:201px;background:linear-gradient(150deg,#4d6a4a,#2e3a34 45%,#a9683a 75%,#3a3a3a)" role="img" aria-label="鍛造機械で作業する工場の写真">
  <span class="en">Process</span><span class="ja">製造工程</span><span class="pill">READ MORE</span>
</div>
<div class="abs process" style="left:650px;background:linear-gradient(150deg,#2e3548,#4a5068 40%,#b8743e 70%,#3a3c48)" role="img" aria-label="火花を散らして金属を研削する作業場の写真">
  <span class="en">Facility</span><span class="ja">工場設備</span><span class="pill" style="top:167px">READ MORE</span>
</div>

<!-- recruit -->
<div class="abs recruit-band"></div>
<div class="abs recruit-photo" role="img" aria-label="炉の前で赤熱した金属を鍛造する設備の写真"></div>
<h2 class="abs sec-title" style="left:231px;top:2120px">採用情報</h2>
<p class="abs sec-sub" style="left:231px;top:2164px">Recruit</p>
<p class="abs recruit-text">清良伸銅は一緒に働く仲間を募集しています！</p>
<a class="abs btn" href="#" style="left:231px;top:2244px;width:239px">READ MORE<svg width="7" height="10" viewBox="0 0 7 10"><path d="M1 1l4 4-4 4" fill="none" stroke="#fff"/></svg></a>

<!-- news -->
<h2 class="abs center sec-title" style="top:2439px">お知らせ</h2>
<p class="abs center sec-sub" style="top:2484px">News</p>

<div class="abs news-rule" style="top:2525px"></div>
<p class="abs news-date" style="top:2549px">2022/08/30</p>
<p class="abs news-title" style="top:2574px">【採用】中途採用の募集を開始しました。</p>
<div class="abs news-rule" style="top:2619px"></div>
<p class="abs news-date" style="top:2643px">2022/08/30</p>
<p class="abs news-title" style="top:2668px">【採用】中途採用の募集を開始しました。</p>
<div class="abs news-rule" style="top:2713px"></div>
<p class="abs news-date" style="top:2736px">2022/08/30</p>
<p class="abs news-title" style="top:2761px">【採用】中途採用の募集を開始しました。</p>
<div class="abs news-rule" style="top:2806px"></div>

<!-- footer -->
<footer class="abs footer">
  <a href="#" style="left:280px">清良伸銅とは</a>
  <a href="#" style="left:414px">製品紹介</a>
  <a href="#" style="left:549px">製造案内</a>
  <a href="#" style="left:684px">採用情報</a>
  <a href="#" style="left:818px">お知らせ</a>
  <p class="abs copyright">Copyright© 2022 清良伸銅株式会社 All Rights Reserved.</p>
</footer>

</body>
</html>
```